Tessaro Lane Website

We are starting a marketing company and to do that we need a website! We want a website that will inspire and persuade to bring out the awesomeness in our clients.
What we want to see:
- Inspirational and persuasive imagery that relate to Branding.
- No cliche images eg. business man, suits and hand shakes
- We want to transform and educate our clients.
- We want to show them the path and would like our website to really act as a guide that guides them step by step through our process.
- We want the portray that we are an investment but not have a pretentious way to it. We put our heart into every project and that is how we treat our clients.
-When you submit your design please include what platform you have created for. Preference would be Wordpress or Joobla.

We have included the psd file for the wire frame, logo files, font files, site map and a link to a video we create to give you more information on what we would like to see. http://clipvault-demo.example/t/qx903LmaP

Feel free to make small modification to the logos if you think it will improve it. Your creativity and advice is most welcome.

One thing we forgot. We would like to have our contact information near the top of the website as well as at the bottom.  Here is out contact info:

Email: info@tessarolane.ca
Phone: 555-013-4829

Reason: As we are new with the platform and that we want to optimize our results, we decided to extend the deadline by 15 days. Thanks!

Target Market(s)

28-60, Male and Female, Oil field, Local Businesses, Dentists, Chiropractors, Hair salon, Construction/Renovation, Events etc

Industry/Entity Type

Investment

Requirements
Must have
• - 4 Inspirational and persuasive Imagery for the top portion of the website
- Must have a feel as if your not on a website an example of this is linked below.
http://www.pitchgallery-demo.example/design/482907/web-design-by-dalia-fenwick
Nice to have
• - Creative advice from you.
- Creative buttons for Get Free Quote and Subscribe buttons. Something out of the box that draws peoples attention. eg. a 'B' button. Just and example but still something related to branding.
Should not have
• No Cliches

```html
<!DOCTYPE html>
<html lang="en">
<head>
<meta charset="utf-8">
<title>Tessaro Lane</title>
<link href="https://fonts.googleapis.com/css2?family=Open+Sans:ital,wght@0,400;0,600;0,700;1,600&family=Paytone+One&display=swap" rel="stylesheet">
<style>
:root{
  --ink:#2b2b2b;
  --body:#5a5a5a;
  --green:#6f9a12;
  --green-light:#9cc23a;
  --green-dark:#3f7a12;
  --cream:#f1e2a6;
  --page:#f7f7f7;
  --bar-top:#8a8b80;
  --bar-bottom:#3a3a38;
  --panel:#e4e4e4;
  --grey-dot:#8c8c8c;
}
*{margin:0;padding:0;box-sizing:border-box}
html,body{width:1200px;height:1113px;overflow:hidden}
body{position:relative;background:var(--page);font-family:"Open Sans",sans-serif;color:var(--body)}
.abs{position:absolute}

.top-bar{left:0;top:0;width:1200px;height:42px;background:linear-gradient(#9a9b90,#55564f);border-bottom:1px solid #333}
.contact-line{display:flex;align-items:center;gap:6px;color:#fff;font-size:17px}
.contact-line b{font-weight:700}
.contact-line svg{fill:currentColor}
.top-bar .contact-line{position:absolute;right:19px;top:9px}

.hero{left:0;top:42px;width:1200px;height:381px;background:linear-gradient(90deg,#efe0a4,#f3e6b4 50%,#f0e0a2);border-bottom:1px solid #ddd;overflow:hidden}
.hero-photo{left:350px;top:0;width:600px;height:381px;background:radial-gradient(ellipse at 50% 55%,#d9c7a0 0%,#c9b7a6 30%,rgba(215,190,160,.5) 60%,rgba(240,224,164,0) 80%)}
.side-panel{left:118px;top:0;width:231px;height:340px;background:linear-gradient(#fff,#eee 55%,rgba(238,238,238,0))}
.brand{left:16px;top:18px;font-size:27px;font-weight:700;color:#555;display:flex;align-items:center;gap:8px}
.brand i{width:12px;height:12px;background:var(--green-light);border-radius:50%;display:block}
.tagline{left:44px;top:77px;font-style:italic;font-weight:600;font-size:13px;color:#333}
.main-nav{left:17px;top:125px;list-style:none}
.main-nav li{font-weight:700;font-size:16px;color:#333;height:37.5px}
.steps{right:20px;top:72px;list-style:none;text-align:right}
.steps li{font-family:"Paytone One",sans-serif;font-size:17px;color:#222;height:68.5px;display:flex;justify-content:flex-end;align-items:flex-start;gap:7px}
.steps li::after{content:"";width:17px;height:17px;border-radius:50%;background:radial-gradient(circle at 40% 35%,#d0d0d0,var(--grey-dot) 60%,#555);margin-top:3px}
.steps li.active{color:var(--green)}
.steps li.active::after{background:radial-gradient(circle at 40% 35%,#d8f08a,var(--green-light) 60%,#4d7a0a)}
.caption{left:400px;top:318px;width:480px;text-align:center;color:#111;font-size:17.5px;line-height:23px}

.box{top:447px;height:94px;background:repeating-linear-gradient(45deg,#e6e6e6 0 2px,#dedede 2px 4px);box-shadow:0 14px 12px -10px rgba(0,0,0,.35)}
.connect{left:120px;width:228px}
.box-title{font-family:"Open Sans",sans-serif;font-weight:700;font-size:21px;color:#555}
.connect .box-title{position:absolute;left:22px;top:16px}
.socials{left:24px;top:48px;display:flex;gap:8px}
.socials span{width:31px;height:31px;border-radius:3px;background:linear-gradient(#8a8a8a,#5e5e5e);display:block}
.newsletter{left:361px;width:711px}
.newsletter .box-title{position:absolute;left:53px;top:10px;font-size:23px}
.newsletter .box-title em{font-style:normal;color:var(--green)}
.email-field{left:54px;top:46px;width:521px;height:39px;background:linear-gradient(#fff,#f0f0f0);border:1px solid #c8c8c8;border-radius:3px;font-size:14px;color:#666;padding:7px 10px}
.subscribe{left:557px;top:47px;width:102px;height:38px;border-radius:3px;background:linear-gradient(#bcbcbc,#8e8e8e);color:#fff;font-weight:700;font-size:16px;text-align:center;line-height:37px;left:918px}

.welcome{left:123px;top:580px;font-family:"Paytone One",sans-serif;font-size:24px;color:#2b2b2b;letter-spacing:.2px}
.mission{left:125px;top:624px;width:940px}
.mission h3{color:var(--green-dark);font-size:16px;font-weight:700;line-height:21px}
.mission p{font-size:15.4px;line-height:21px}
.checks{left:127px;top:720px;list-style:none}
.checks li{display:flex;align-items:center;gap:11px;font-size:16px;color:#333;height:34.6px}
.checks svg{flex:none}
.quote{left:919px;top:832px;width:157px;height:40px;border-radius:3px;background:linear-gradient(#6fb21f,var(--green-dark));color:#fff;font-weight:700;font-size:16px;text-align:center;line-height:40px;box-shadow:0 1px 2px rgba(0,0,0,.3)}
.closing{left:125px;top:906px;width:940px;font-size:15.4px;line-height:21px}

.footer{left:0;top:994px;width:1200px;height:119px;background:linear-gradient(#9a9a98,var(--bar-bottom))}
.footer-nav{left:123px;top:32px;display:flex;gap:14px;list-style:none;color:#fff;font-size:17px}
.copyright{left:123px;top:59px;color:var(--green-light);font-size:17px}
.footer .contact-line{position:absolute;right:124px;top:33px}
</style>
</head>
<body>

<header class="top-bar abs">
  <div class="contact-line">
    <svg width="16" height="12" viewBox="0 0 16 12"><path d="M0 0h16v12H0z M1 1l7 6 7-6" fill="#111" stroke="#ddd" stroke-width=".8"/></svg>
    <span>info@tessarolane.ca</span><span>|</span>
    <svg width="14" height="14" viewBox="0 0 24 24"><path fill="#111" d="M6.6 10.8a15 15 0 0 0 6.6 6.6l2.2-2.2c.3-.3.7-.4 1-.2 1.1.4 2.3.6 3.6.6.6 0 1 .4 1 1V20c0 .6-.4 1-1 1A17 17 0 0 1 3 4c0-.6.4-1 1-1h3.5c.6 0 1 .4 1 1 0 1.3.2 2.5.6 3.6.1.3 0 .7-.2 1z"/></svg>
    <b>555-013-4829</b>
  </div>
</header>

<section class="hero abs">
  <div class="hero-photo abs" role="img" aria-label="Photo of three young girls sharing a whispered secret"></div>
  <div class="side-panel abs">
    <div class="brand abs"><i></i>Tessaro Lane</div>
    <div class="tagline abs">Because You´re Awesome!</div>
    <ul class="main-nav abs">
      <li>STRATEGY</li><li>PORTFOLIO</li><li>ABOUT US</li><li>CONTACT US</li><li>BLOG</li>
    </ul>
  </div>
  <ul class="steps abs">
    <li>TESSARO LANE</li><li>BE FOUND</li><li class="active">CONNECT</li><li>GET GROWING</li>
  </ul>
  <p class="caption abs">It's your chance to engage your audience and lead the conversation. It's the new word of mouth</p>
</section>

<div class="box connect abs">
  <div class="box-title">CONNECT WITH US</div>
  <div class="socials abs" aria-label="Social links"><span></span><span></span><span></span><span></span><span></span></div>
</div>
<div class="box newsletter abs">
  <div class="box-title"><em>GET TIPS AND TRICKS!</em> SUBSCRIBE TO OUR NEWSLETTER</div>
  <div class="email-field abs">your email id</div>
</div>
<div class="subscribe abs" style="top:494px">Subscribe</div>

<h1 class="welcome abs">WELCOME TO TESSARO LANE</h1>
<div class="mission abs">
  <h3>Our Mission</h3>
  <p>Etiam adipiscing mollis nulla, ac bibendum elit commodo ac. Pellentesque vehicula sodales vulputate. Suspendisse vel semper tortor. Duis tristique pharetra ligula sed bibendum. Etiam adipiscing mollis nulla, ac bibendum elit commodo ac. Etiam adipiscing mollis nulla, ac bibendum elit commodo ac.</p>
</div>
<ul class="checks abs">
  <li><svg width="20" height="20" viewBox="0 0 20 20"><rect width="20" height="20" rx="3" fill="#8cbb2c"/><path d="M5 10.5l3.3 3.2L15 6.8" fill="none" stroke="#fff" stroke-width="2.6"/></svg>Nam ac risus metus, sit amet blandit ante.</li>
  <li><svg width="20" height="20" viewBox="0 0 20 20"><rect width="20" height="20" rx="3" fill="#8cbb2c"/><path d="M5 10.5l3.3 3.2L15 6.8" fill="none" stroke="#fff" stroke-width="2.6"/></svg>Nunc adipiscing, ipsum eu scelerisque euismod, diam nisl condimentum neque,</li>
  <li><svg width="20" height="20" viewBox="0 0 20 20"><rect width="20" height="20" rx="3" fill="#8cbb2c"/><path d="M5 10.5l3.3 3.2L15 6.8" fill="none" stroke="#fff" stroke-width="2.6"/></svg>Vel gravida ligula velit vitae nisl. Pellentesque at dignissim ipsum. Vivamus id massa arcu.</li>
  <li><svg width="20" height="20" viewBox="0 0 20 20"><rect width="20" height="20" rx="3" fill="#8cbb2c"/><path d="M5 10.5l3.3 3.2L15 6.8" fill="none" stroke="#fff" stroke-width="2.6"/></svg>Phasellus feugiat condimentum neque ac bibendum.</li>
  <li><svg width="20" height="20" viewBox="0 0 20 20"><rect width="20" height="20" rx="3" fill="#8cbb2c"/><path d="M5 10.5l3.3 3.2L15 6.8" fill="none" stroke="#fff" stroke-width="2.6"/></svg>Pellentesque dictum lectus sapien, eu pulvinar eros.</li>
</ul>
<div class="quote abs">Get a Free Quote!</div>
<p class="closing abs">Maecenas lacinia, nulla at interdum dapibus, velit sapien posuere eros, et hendrerit purus erat quis est. Proin commodo blandit mauris sed convallis. Donec tellus metus, feugiat sed condimentum congue, dignissim ut leo.</p>

<footer class="footer abs">
  <ul class="footer-nav abs"><li>Site Map</li><li>Strategy</li><li>Portfolio</li><li>About Us</li><li>Contact Us</li><li>Blog</li></ul>
  <div class="copyright abs">©TESSARO LANE INC. 2013</div>
  <div class="contact-line">
    <svg width="16" height="12" viewBox="0 0 16 12"><path d="M0 0h16v12H0z M1 1l7 6 7-6" fill="#111" stroke="#ddd" stroke-width=".8"/></svg>
    <span>info@tessarolane.ca</span><span>|</span>
    <svg width="14" height="14" viewBox="0 0 24 24"><path fill="#111" d="M6.6 10.8a15 15 0 0 0 6.6 6.6l2.2-2.2c.3-.3.7-.4 1-.2 1.1.4 2.3.6 3.6.6.6 0 1 .4 1 1V20c0 .6-.4 1-1 1A17 17 0 0 1 3 4c0-.6.4-1 1-1h3.5c.6 0 1 .4 1 1 0 1.3.2 2.5.6 3.6.1.3 0 .7-.2 1z"/></svg>
    <b>555-013-4829</b>
  </div>
</footer>

</body>
</html>
```